Business Card / Appointment Card for Physician

On one side it should give the logo, address, and contact information, and on the other side it should br an Appointment card.

One Side:
Logo (see attached files)
Board Certified American Orthopedic Surgery

1487 Harrowgate Ave.
Suite KM7
Bronx, NY 10527
Tel: (718) 552 - 1948
Fax: (718) 552 - 7210

628 Fourth Ave.
Suite 42
New York, NY 10087
Tel: (212) 734 - 2815

Second Side:
Appointment
give them a choice of Bronx or Mahattan office
For:
Date:
Time:

If you are unable to keep your appointment, please call (718) 263-5102 24hrs in advance.

Target Market(s)

People that need orthopedic surgery

Industry/Entity Type

Business

Contact Information for Business Card

smart and attractive

Requirements
Must have
• logo
• contact information on one side, appointment information on the other

```html
<!DOCTYPE html>
<html lang="en">
<head>
<meta charset="utf-8">
<title>Daniel R. Holloway MD PC – Business and Appointment Card</title>
<link rel="stylesheet" href="https://fonts.googleapis.com/css2?family=Inter:wght@300;600&family=Didact+Gothic&family=Archivo:wght@800&display=swap">
<style>
  :root {
    --backdrop: #2c2c2c;
    --card: #ffffff;
    --brand-blue: #276496;
    --ink: #1a1a1a;
    --line: #6b6b6b;
  }
  * { box-sizing: border-box; margin: 0; padding: 0; }
  html, body { width: 1200px; height: 914px; overflow: hidden; background: var(--backdrop); }
  .card {
    position: absolute;
    left: 329px;
    width: 543px;
    height: 334px;
    background: var(--card);
    overflow: hidden;
  }
  .card--front { top: 111px; }
  .card--back { top: 470px; }

  /* Front */
  .front__brand {
    position: absolute; left: 0; top: 0; width: 245px; height: 100%;
    text-align: center;
  }
  .brand-mark__dot {
    position: absolute; left: 97px; top: 99px;
    width: 50px; height: 50px; border-radius: 50%;
    background: var(--brand-blue);
  }
  .brand-mark__name {
    position: absolute; left: 0; right: 0; top: 160px;
    font-family: "Inter", sans-serif; font-weight: 600;
    font-size: 15px; line-height: 18px; color: var(--brand-blue); letter-spacing: -0.3px;
  }
  .front__tagline {
    position: absolute; left: 0; right: 0; top: 188px;
    font-family: "Inter", sans-serif; font-weight: 300;
    font-size: 15px; line-height: 21px; color: var(--ink);
  }
  .front__contact {
    position: absolute; left: 245px; top: 0; width: 298px; height: 100%;
    background: var(--brand-blue);
    color: #fff; text-align: right;
    font-family: "Inter", sans-serif; font-weight: 300;
    font-size: 15.5px; line-height: 21px;
  }
  .office { position: absolute; right: 43px; font-style: normal; }
  .office--bronx { top: 53px; }
  .office--manhattan { top: 199px; }

  /* Back */
  .appt__title {
    position: absolute; left: 329px; width: 543px; top: 502px; text-align: center;
    font-family: "Archivo", sans-serif; font-weight: 800;
    font-size: 19px; line-height: 24px; letter-spacing: 0.5px; color: #000;
  }
  .appt__note, .appt__field, .appt__footer {
    font-family: "Didact Gothic", sans-serif; color: var(--ink);
  }
  .appt__note {
    position: absolute; left: 374px; top: 526px; font-size: 17px; line-height: 22px; letter-spacing: 0.4px;
  }
  .appt__field {
    position: absolute; left: 369px; width: 465px; height: 29px;
    border: 1px solid var(--line);
    font-size: 17px; line-height: 27px; padding-left: 6px;
  }
  .appt__footer {
    position: absolute; left: 329px; width: 543px; top: 726px;
    text-align: center; font-size: 16px; line-height: 21px; letter-spacing: 2.6px;
  }
</style>
</head>
<body>
  <section class="card card--front">
    <div class="front__brand">
      <span class="brand-mark__dot"></span>
      <p class="brand-mark__name">DANIEL R. HOLLOWAY MD PC</p>
      <p class="front__tagline">Board Certified American<br>Orthopedic Surgery</p>
    </div>
    <div class="front__contact">
      <address class="office office--bronx">
        1487 Harrowgate Ave.<br>Suite KM7<br>Bronx, NY 10527<br>Tel: (718) 552 - 1948<br>Fax: (718) 552 - 7210
      </address>
      <address class="office office--manhattan">
        628 Fourth Ave.<br>Suite 42<br>New York, NY 10087<br>Tel: (212) 734 - 2815
      </address>
    </div>
  </section>

  <section class="card card--back"></section>
  <h1 class="appt__title">APPOINTMENT</h1>
  <p class="appt__note">Give them a choice of Bronx or Mahattan office</p>
  <div class="appt__field" style="top:564px">For &nbsp;&nbsp;&nbsp;:</div>
  <div class="appt__field" style="top:602px">Date :</div>
  <div class="appt__field" style="top:641px">Time &nbsp;:</div>
  <div class="appt__field" style="top:679px"></div>
  <p class="appt__footer">If you are unable to keep your appointment,<br>please call (718) 263-5102 24hrs in advance.</p>
</body>
</html>
```